Flyer Design

I'm looking for a new flyer design to help promote our landscape company, and some of our main service for the up and coming season. We're trying to position ourselves as a leader in our market, so obviously quality is important to us.

Our current promotion is 25% off the first month with signup of annual service.

Phone Number: (816) 555-0193
Website: gardelvista.com
Our tagline: "Your hands are full... Let us help"

The call to action: direct them to our website for a detailed list of services and to receive a free quote.

You're welcome to add your own wording and punctuation. If I like the design I will provide feedback accordingly.

I have attached a jpg of our logo to help with design colors. I will provide the vector file upon completion of this project.

Also, I've attached a few photos that I had on hand of our companies work that may help with the design. Obviously I don't want to use them all, but there are a couple just to help out. I'm not opposed to stock photos either.
Thanks

Target Market(s)

We market to high end customers, generally with home between $500k-$2mil, or household income over $200k. Quality and creativity are most important to us.

Industry/Entity Type

Landscape

Requirements
Must have
• Creativity, easy to read, modern style.

```html
<!DOCTYPE html>
<html lang="en">
<head>
<meta charset="utf-8">
<title>Gardel Vista – Lawn &amp; Garden Flyer</title>
<link rel="stylesheet" href="https://fonts.googleapis.com/css2?family=Oswald:wght@300;400;500&family=Great+Vibes&family=Roboto:wght@400;700&display=swap">
<style>
  :root {
    --page: #ffffff;
    --black: #000000;
    --white: #ffffff;
    --red: #e0483a;
    --red-bright: #e8513f;
    --wine: #8e0b2c;
    --cream: #f1efea;
    --ink: #222222;
    --green: #5a9a36;
    --green-deep: #4c8a2c;
    --autumn: #d46a2a;
    --autumn-deep: #c2561f;
  }
  * { margin: 0; padding: 0; box-sizing: border-box; }
  html, body { width: 1200px; height: 1000px; overflow: hidden; background: var(--page); }
  .canvas { position: relative; width: 1200px; height: 1000px; }
  .flyer {
    position: absolute; left: 156px; top: 158px; width: 912px; height: 702px;
    background: var(--black); overflow: hidden;
    box-shadow: 0 0 3px rgba(0,0,0,0.25);
  }
  .brand-panel {
    position: absolute; left: 0; top: 0; width: 307px; height: 207px;
    background: var(--cream);
    display: flex; align-items: center; justify-content: center; gap: 12px;
  }
  .brand-dot { width: 24px; height: 24px; border-radius: 50%; background: var(--red); }
  .brand-name {
    font-family: 'Oswald', sans-serif; font-weight: 500; font-size: 42px;
    color: var(--ink); text-transform: uppercase; letter-spacing: 1px;
  }
  .photo { position: absolute; }
  .photo-lawn { background: linear-gradient(180deg, var(--green) 0%, var(--green-deep) 100%); }
  .photo-autumn { background: linear-gradient(180deg, var(--autumn) 0%, var(--autumn-deep) 100%); }
  .photo-brick-house { left: 0; top: 212px; width: 307px; height: 183px; }
  .photo-suburban-home { left: 0; top: 400px; width: 307px; height: 182px; }
  .photo-mower { left: 619px; top: 0; width: 293px; height: 140px; }
  .photo-leaves { left: 619px; top: 145px; width: 293px; height: 137px; }
  .photo-garden-path { left: 619px; top: 287px; width: 293px; height: 139px; }

  .services { position: absolute; left: 366px; top: 44px; width: 250px; }
  .services-title {
    font-family: 'Oswald', sans-serif; font-weight: 400; color: var(--red-bright);
    font-size: 27px; line-height: 34px; font-variant: small-caps; letter-spacing: -0.8px;
    margin-bottom: 6px;
  }
  .services-list { list-style: none; }
  .services-list li {
    position: relative; padding-left: 25px;
    font-family: 'Oswald', sans-serif; font-weight: 400; color: var(--white);
    font-size: 18px; line-height: 32.2px; letter-spacing: -0.7px;
  }
  .services-list li .cont { display: block; }
  .services-list svg { position: absolute; left: 0; top: 11px; }
  .tagline {
    position: absolute; left: 358px; top: 484px; width: 280px;
    font-family: 'Great Vibes', cursive; color: var(--white);
    font-size: 38px; line-height: 38px;
  }

  .promo { position: absolute; left: 680px; top: 438px; width: 180px; height: 172px; }
  .promo-text { position: absolute; left: 0; top: 0; width: 170px; text-align: center; color: var(--white); font-family: 'Roboto', sans-serif; }
  .promo-figure { position: absolute; top: 14px; left: 0; width: 170px; font-weight: 700; font-size: 44px; line-height: 50px; }
  .promo-figure small { font-size: 28px; }
  .promo-note { position: absolute; top: 72px; left: 8px; width: 154px; font-size: 13px; line-height: 15px; }

  .footer-band {
    position: absolute; left: 0; top: 584px; width: 912px; height: 118px;
    background: linear-gradient(90deg, var(--red) 0%, var(--red) 45%, var(--wine) 100%);
  }
  .social { position: absolute; left: 33px; top: 34px; display: flex; gap: 11px; }
  .social span { width: 50px; height: 50px; border-radius: 50%; background: rgba(255,255,255,0.28); }
  .contact { position: absolute; right: 46px; top: 18px; text-align: right; color: var(--white); font-family: 'Oswald', sans-serif; }
  .contact-phone { font-size: 18px; font-weight: 300; letter-spacing: -0.8px; line-height: 36px; }
  .contact-phone strong { font-weight: 400; font-size: 29px; letter-spacing: -0.5px; }
  .contact-web { font-size: 18px; font-weight: 300; letter-spacing: -0.9px; line-height: 36px; }
  .contact-web strong { font-weight: 400; font-size: 30px; letter-spacing: -0.5px; }
</style>
</head>
<body>
<div class="canvas">
  <div class="flyer">
    <div class="brand-panel">
      <span class="brand-dot"></span>
      <span class="brand-name">Gardel Vista</span>
    </div>
    <div class="photo photo-lawn photo-brick-house" role="img" aria-label="Photo: brick cottage with a freshly mown lawn"></div>
    <div class="photo photo-lawn photo-suburban-home" role="img" aria-label="Photo: suburban home with trimmed shrubs and front lawn"></div>
    <div class="photo photo-lawn photo-mower" role="img" aria-label="Photo: ride-on mower cutting a striped lawn"></div>
    <div class="photo photo-autumn photo-leaves" role="img" aria-label="Photo: rake gathering autumn leaves"></div>
    <div class="photo photo-lawn photo-garden-path" role="img" aria-label="Photo: garden path through flower beds"></div>

    <section class="services">
      <h2 class="services-title">Solutions for your<br>lawn &amp; garden:</h2>
      <ul class="services-list">
        <li><svg width="20" height="10" viewBox="0 0 20 10"><path d="M0 0h6l5 5-5 5H0l5-5z M9 0h6l5 5-5 5H9l5-5z" fill="#e8513f"/></svg>Weekly Lawn Service</li>
        <li><svg width="20" height="10" viewBox="0 0 20 10"><path d="M0 0h6l5 5-5 5H0l5-5z M9 0h6l5 5-5 5H9l5-5z" fill="#e8513f"/></svg>Spring &amp; Fall Cleanup</li>
        <li><svg width="20" height="10" viewBox="0 0 20 10"><path d="M0 0h6l5 5-5 5H0l5-5z M9 0h6l5 5-5 5H9l5-5z" fill="#e8513f"/></svg>Core Aeration Service</li>
        <li><svg width="20" height="10" viewBox="0 0 20 10"><path d="M0 0h6l5 5-5 5H0l5-5z M9 0h6l5 5-5 5H9l5-5z" fill="#e8513f"/></svg>Turf Edging</li>
        <li><svg width="20" height="10" viewBox="0 0 20 10"><path d="M0 0h6l5 5-5 5H0l5-5z M9 0h6l5 5-5 5H9l5-5z" fill="#e8513f"/></svg>Landscape Renovation</li>
        <li><svg width="20" height="10" viewBox="0 0 20 10"><path d="M0 0h6l5 5-5 5H0l5-5z M9 0h6l5 5-5 5H9l5-5z" fill="#e8513f"/></svg>Brush &amp; Tree Trimming</li>
        <li><svg width="20" height="10" viewBox="0 0 20 10"><path d="M0 0h6l5 5-5 5H0l5-5z M9 0h6l5 5-5 5H9l5-5z" fill="#e8513f"/></svg>Ornamental Tree Care</li>
        <li><svg width="20" height="10" viewBox="0 0 20 10"><path d="M0 0h6l5 5-5 5H0l5-5z M9 0h6l5 5-5 5H9l5-5z" fill="#e8513f"/></svg>Mulch Bed Renovation</li>
        <li><svg width="20" height="10" viewBox="0 0 20 10"><path d="M0 0h6l5 5-5 5H0l5-5z M9 0h6l5 5-5 5H9l5-5z" fill="#e8513f"/></svg>Gutter Cleaning</li>
        <li><svg width="20" height="10" viewBox="0 0 20 10"><path d="M0 0h6l5 5-5 5H0l5-5z M9 0h6l5 5-5 5H9l5-5z" fill="#e8513f"/></svg>Snow Removal &amp;<span class="cont">Ice Management</span></li>
      </ul>
    </section>

    <p class="tagline">Your hands are<br>full... Let us help!</p>

    <footer class="footer-band">
      <div class="social" aria-label="Social links">
        <span></span><span></span><span></span>
      </div>
      <div class="contact">
        <div class="contact-phone">Phone: <strong>(816) 555-0193</strong></div>
        <div class="contact-web">For more details visit our website: <strong>gardelvista.com</strong></div>
      </div>
    </footer>

    <div class="promo">
      <svg width="180" height="172" viewBox="0 0 180 172">
        <path d="M30 20 C50 2, 120 2, 145 18 C175 30, 175 115, 140 135 C115 148, 60 148, 40 135 L25 168 L22 128 C0 110, 0 40, 30 20 Z"
              fill="#e0483a" stroke="#ffffff" stroke-width="4"/>
      </svg>
      <div class="promo-text">
        <div class="promo-figure">-25<small>%</small></div>
        <div class="promo-note">the first month<br>with signup of annual<br>service</div>
      </div>
    </div>
  </div>
</div>
</body>
</html>
```